We need a refreshed business card. Our company is a venture capital investment firm focused on investing in medical devices. Logo is attached. please also see our website www.velmoracapital.example

Target Market(s)

investors and potential investment targets

Industry/Entity Type

medical investments

Contact Information for Business Card

logo, name, title, email, phone, website, address,

Colors
0054AA
0677BA
7BADD7
CADEEF
E8F1F8
0094D4
00A9DD
6FCCEA
C7EBF8
E9F6FB
00AB8E
00BBA5
67D7C9
C6EFE9
E9F9F6

Requirements
Must have
• fresh modern design
Nice to have
• QR code leading to our linked in page, short description of what we do “Early Stage Medical Device Investors”

```html
<!DOCTYPE html>
<html lang="en">
<head>
<meta charset="utf-8">
<title>Velmora — Business Card</title>
<link href="https://fonts.googleapis.com/css2?family=Ubuntu:wght@300;400;500&display=swap" rel="stylesheet">
<style>
  :root {
    --blue-deep: #0054AA;
    --blue-mid: #0677BA;
    --teal: #00AB8E;
    --teal-bright: #00BBA5;
    --teal-soft: #67D7C9;
    --mist: #E8F1F8;
    --mist-soft: #C7EBF8;
    --ink: #2a2d33;
    --page: #eef2f5;
    --white: #ffffff;
  }
  * { margin: 0; padding: 0; box-sizing: border-box; }
  html, body { width: 960px; height: 1200px; overflow: hidden; }
  body {
    background: radial-gradient(ellipse at 30% 20%, #f6f8fa 0%, var(--page) 60%, #e6edf2 100%);
    font-family: "Ubuntu", sans-serif;
    position: relative;
  }
  .card {
    position: absolute;
    left: 90px;
    width: 780px;
    height: 427px;
    overflow: hidden;
    box-shadow: 0 18px 30px rgba(40, 60, 80, 0.22);
  }
  .card--front { top: 143px;
    background:
      radial-gradient(ellipse 260px 80px at 52% 46%, rgba(160, 195, 215, 0.35), transparent 70%),
      radial-gradient(ellipse 280px 120px at 85% 8%, rgba(180, 210, 225, 0.45), transparent 70%),
      linear-gradient(180deg, #dfe8ee 0%, #f3f6f8 45%, var(--white) 80%);
  }
  .card--back { top: 630px;
    background:
      linear-gradient(200deg, var(--teal-bright) 0%, rgba(0, 84, 170, 0) 30%),
      linear-gradient(160deg, var(--teal-bright) 0%, var(--blue-mid) 30%, var(--blue-deep) 50%, var(--blue-mid) 75%, #0060a8 100%);
  }
  .brand {
    position: absolute;
    display: flex;
    align-items: center;
    gap: 14px;
    font-weight: 500;
    letter-spacing: -1px;
  }
  .brand__dot { width: 18px; height: 18px; border-radius: 50%; }
  .card--front .brand { left: 58px; top: 62px; font-size: 74px; color: var(--blue-deep); }
  .card--front .brand__dot { background: var(--teal); }
  .card--back .brand { left: 0; right: 0; top: 160px; justify-content: center; font-size: 92px; color: var(--white); }
  .card--back .brand__dot { background: var(--white); }
  .person { position: absolute; left: 61px; top: 222px; }
  .person__name { font-size: 25px; color: var(--ink); font-weight: 500; line-height: 1; }
  .person__name span { font-weight: 300; }
  .person__title { font-size: 19px; color: var(--teal); font-weight: 300; margin-top: 3px; }
  .contacts { position: absolute; left: 61px; top: 296px; list-style: none; }
  .contacts li { display: flex; align-items: center; gap: 16px; font-size: 16px; color: var(--ink); height: 26px; }
  .contacts svg { width: 16px; height: 16px; fill: var(--teal); flex: none; }
  .band {
    position: absolute; left: 0; right: 0; bottom: 0; height: 40px;
    background:
      radial-gradient(ellipse 80px 20px at 88% 100%, rgba(0, 84, 170, 0.9), transparent 80%),
      linear-gradient(90deg, var(--teal-bright) 0%, var(--teal) 15%, var(--blue-mid) 45%, #05809f 100%);
    display: flex; align-items: center; justify-content: center;
  }
  .band__url { font-size: 12px; color: var(--white); letter-spacing: 4px; text-transform: uppercase; font-weight: 300; margin-right: 60px; }
</style>
</head>
<body>
  <section class="card card--front">
    <div class="brand"><span class="brand__dot"></span>Velmora</div>
    <div class="person">
      <p class="person__name">Daniel <span>Marlow</span></p>
      <p class="person__title">Chief Executive Officer</p>
    </div>
    <ul class="contacts">
      <li><svg viewBox="0 0 24 24" aria-hidden="true"><path d="M6.6 10.8a15.1 15.1 0 0 0 6.6 6.6l2.2-2.2a1 1 0 0 1 1-.25 11.4 11.4 0 0 0 3.6.57 1 1 0 0 1 1 1V20a1 1 0 0 1-1 1A17 17 0 0 1 3 4a1 1 0 0 1 1-1h3.5a1 1 0 0 1 1 1c0 1.25.2 2.45.57 3.57a1 1 0 0 1-.25 1z"/></svg>214-555-0187</li>
      <li><svg viewBox="0 0 24 24" aria-hidden="true"><path d="M12 2a10 10 0 1 0 5 18.7l-1-1.7A8 8 0 1 1 20 12v1.5a1.5 1.5 0 0 1-3 0V12a5 5 0 1 0-1.5 3.6A3.5 3.5 0 0 0 22 13.5V12A10 10 0 0 0 12 2zm0 13a3 3 0 1 1 0-6 3 3 0 0 1 0 6z"/></svg>info@velmoracapital.example</li>
      <li><svg viewBox="0 0 24 24" aria-hidden="true"><path d="M12 2a7 7 0 0 0-7 7c0 5.2 7 13 7 13s7-7.8 7-13a7 7 0 0 0-7-7zm0 9.5A2.5 2.5 0 1 1 12 6.5a2.5 2.5 0 0 1 0 5z"/></svg>2210 Harbor Crest Dr., Suite 410 Dallas, TX 75201</li>
    </ul>
    <div class="band"><span class="band__url">www.velmoracapital.example</span></div>
  </section>

  <section class="card card--back">
    <div class="brand"><span class="brand__dot"></span>Velmora</div>
  </section>
</body>
</html>
```